Flyer for Beach Party required

We need a flyer for a weekly beach party we hold at our beach club. There is a live dj but it is more of a loungey-party and not a nightclub/sorrel cove style party.

We need to emphasise there is a dj and use files and graphics from our beach club (you can check out our instagram and i can send you originals of any files required.. please see BRIEF.TXT file for all of our social media/contact details)

The brief also contains more details on the project.

Club

```html
<!DOCTYPE html>
<html lang="en">
<head>
<meta charset="utf-8">
<title>Friday Beach Lounge Party — Palmera Beach</title>
<link rel="stylesheet" href="https://fonts.googleapis.com/css2?family=Ubuntu:ital,wght@0,300;0,400;0,500;1,300;1,400;1,500;1,700&family=Montserrat:wght@300;400&display=swap">
<style>
  :root {
    --sky-top: #b8581f;
    --sky-glow: #f2a23a;
    --sun: #fff4c8;
    --sea: #e08a2c;
    --sand-dark: #3f4852;
    --sand-deep: #2b323b;
    --white: #ffffff;
    --logo-gold: #e9c27e;
    --footer-orange: #d8622c;
    --icon-ink: #3a2a22;
  }
  * { box-sizing: border-box; margin: 0; padding: 0; }
  html, body {
    width: 1200px;
    height: 1200px;
    overflow: hidden;
    background: #ffffff;
  }
  .flyer {
    position: relative;
    width: 1200px;
    height: 1200px;
    overflow: hidden;
    font-family: "Ubuntu", sans-serif;
    color: var(--white);
  }
  .beach-scene {
    position: absolute;
    inset: 0;
    background:
      radial-gradient(circle at 636px 432px, var(--sun) 0, #ffd76a 45px, rgba(245,170,60,0.85) 150px, rgba(245,170,60,0) 420px),
      linear-gradient(180deg,
        var(--sky-top) 0%,
        #d9792a 22%,
        var(--sky-glow) 40%,
        var(--sea) 50%,
        #b86a2e 60%,
        #6a5a52 68%,
        var(--sand-dark) 78%,
        var(--sand-deep) 100%);
  }
  .headline {
    position: absolute;
    top: 128px;
    left: 0;
    width: 100%;
    text-align: center;
    font-style: italic;
    font-weight: 400;
    font-size: 88px;
    line-height: 118px;
    letter-spacing: 1px;
    text-shadow: 0 2px 10px rgba(120,50,10,0.35);
  }
  .venue-name {
    position: absolute;
    left: 54px;
    top: 834px;
    display: flex;
    align-items: center;
    gap: 14px;
    font-weight: 500;
    font-size: 58px;
    line-height: 1;
    color: var(--logo-gold);
  }
  .venue-name .mark {
    width: 30px;
    height: 30px;
    border-radius: 50%;
    background: var(--logo-gold);
    flex: none;
  }
  .venue-name .word { display: block; }
  .venue-name .word small {
    display: block;
    font-size: 58px;
    margin-top: 22px;
  }
  .host {
    position: absolute;
    left: 360px;
    top: 932px;
  }
  .host .hosted-by {
    font-style: italic;
    font-weight: 700;
    font-size: 41px;
    line-height: 1;
  }
  .host .resident {
    font-weight: 400;
    font-size: 25px;
    line-height: 1;
    margin-top: 12px;
  }
  .dj-name {
    position: absolute;
    left: 583px;
    top: 944px;
    font-family: "Montserrat", sans-serif;
    font-weight: 300;
    font-size: 76px;
    line-height: 1;
    letter-spacing: 26px;
  }
  .promo {
    position: absolute;
    left: 884px;
    top: 932px;
    line-height: 1;
  }
  .promo .lead {
    font-size: 35px;
    font-weight: 400;
  }
  .promo .free {
    font-size: 56px;
    margin-top: 4px;
  }
  .promo .free em { font-style: italic; font-weight: 500; }
  .promo .free span { font-weight: 400; }
  .contact-bar {
    position: absolute;
    left: 24px;
    top: 1052px;
    width: 1152px;
    height: 88px;
    border-radius: 20px;
    background: var(--footer-orange);
    display: flex;
    align-items: center;
    justify-content: space-between;
    padding: 0 24px 0 40px;
  }
  .contact-item {
    display: flex;
    align-items: center;
    gap: 10px;
    font-size: 21px;
    font-weight: 500;
    white-space: nowrap;
  }
  .contact-item .dot {
    width: 44px;
    height: 44px;
    border-radius: 50%;
    background: var(--white);
    flex: none;
    display: flex;
    align-items: center;
    justify-content: center;
  }
  .contact-item .dot svg { width: 24px; height: 24px; }
  .contact-web {
    font-size: 20px;
    font-weight: 500;
    line-height: 1.3;
    white-space: nowrap;
  }
</style>
</head>
<body>
<main class="flyer">
  <div class="beach-scene" role="img" aria-label="Photo of a sunset over the sea seen from the beach, with white curtained cabanas, parasols and guests lounging on the sand"></div>

  <h1 class="headline">friday beach<br>lounge party</h1>

  <div class="venue-name">
    <span class="mark"></span>
    <span class="word">Palmera<small>beach</small></span>
  </div>

  <div class="host">
    <p class="hosted-by">Hosted by</p>
    <p class="resident">our resident DJ</p>
  </div>

  <p class="dj-name">DJ K</p>

  <div class="promo">
    <p class="lead">promoting a</p>
    <p class="free"><em>free</em> <span>cd</span></p>
  </div>

  <footer class="contact-bar">
    <div class="contact-item"><span class="dot"></span>/palmerabeach</div>
    <div class="contact-item"><span class="dot"></span>@palmerabeach</div>
    <div class="contact-item"><span class="dot"></span>@palmerabeach</div>
    <div class="contact-item">
      <span class="dot">
        <svg viewBox="0 0 24 24" aria-hidden="true"><path fill="#3a2a22" d="M6.6 10.8a15.1 15.1 0 0 0 6.6 6.6l2.2-2.2a1 1 0 0 1 1-.25 11.4 11.4 0 0 0 3.6.57 1 1 0 0 1 1 1V20a1 1 0 0 1-1 1A17 17 0 0 1 3 4a1 1 0 0 1 1-1h3.5a1 1 0 0 1 1 1c0 1.250.2 2.45.57 3.6a1 1 0 0 1-.25 1z"/></svg>
      </span>75120486
    </div>
    <div class="contact-web">info@palmerabeach.ae<br>www.palmerabeach.ae</div>
  </footer>
</main>
</body>
</html>
```